Spring Pet Banner for Veterinary Hospital 5m x 1.2m

Meadowbrook Pet Hospital is a Veterinary Hospital that treats Dogs and Cats. I want a new poster to go on our front fence for spring. It's 5m x 1.2m. I want a design that is eye catching from a nearby road that promotes preventative health measures to get ready for spring.
I have attached images that we commonly use in our branding. I would like images that suite the mood of these images.
EDIT: I have just uploaded a design that I knocked up. I think it sends a clear message.....but I am not a graphic designer or marketing expert, so you can make a similar design if you want and clean it up.

The plan I had for the design is not working. I have simplified the plan so designers can use their own ideas.

Target Market(s)

Women Aged 18 to 60.

Industry/Entity Type

Veterinary

Font styles to use
Sans Serif

Colors
9bcb3b
f78f20
f37122

Requirements
Must have
• Visible from road 30m away.
• Spring.
• A call to action.
• Compliment existing branding.
Nice to have
• Gives people a reason to bring their animals to us now.
Should not have
• Clip art.

```html
<!DOCTYPE html>
<html lang="en">
<head>
<meta charset="utf-8">
<title>Meadowbrook Pet Hospital – Spring Parasite Banner</title>
<link rel="stylesheet" href="https://fonts.googleapis.com/css2?family=Montserrat:wght@400;700;800&display=swap">
<style>
  :root {
    --backdrop: #c9c9c9;
    --paper: #ffffff;
    --green: #5f9a26;
    --green-light: #74ad22;
    --green-title: #4f8a1f;
    --brown: #5a3d1e;
    --orange: #e6560f;
    --orange-light: #f37122;
    --red-ring: #c8232c;
    --ink: #2b2b2b;
  }
  * { box-sizing: border-box; margin: 0; padding: 0; }
  html, body { width: 1200px; height: 1200px; overflow: hidden; }
  body {
    background: var(--backdrop);
    font-family: "Montserrat", sans-serif;
    position: relative;
  }
  .banner {
    position: absolute;
    left: 8px; top: 498px;
    width: 1184px; height: 284px;
    background: var(--paper);
    overflow: hidden;
  }
  .banner-art { position: absolute; inset: 0; }
  .headline {
    position: absolute;
    left: 330px; width: 660px; top: 26px;
    text-align: center;
    font-weight: 800;
    font-size: 26px;
    letter-spacing: -0.3px;
    color: var(--green-title);
  }
  .headline .accent { color: var(--orange); }
  .subline {
    position: absolute;
    left: 330px; width: 660px; top: 58px;
    text-align: center;
    font-size: 16px;
    line-height: 18px;
    color: var(--ink);
  }
  .subline strong { font-weight: 700; }
  .threat-label {
    position: absolute;
    top: 226px;
    transform: translateX(-50%);
    text-align: center;
    color: #fff;
    font-weight: 700;
    font-size: 18px;
    line-height: 18px;
    white-space: nowrap;
  }
  .brand {
    position: absolute;
    left: 1030px; width: 144px; top: 90px;
    text-align: center;
  }
  .brand-dot {
    width: 24px; height: 24px; border-radius: 50%;
    background: var(--green-light);
    margin: 0 auto 12px;
  }
  .brand-name {
    color: var(--brown);
    font-weight: 700;
    font-size: 16px;
    line-height: 20px;
    white-space: nowrap;
  }
  .book-online {
    position: absolute;
    left: 974px; top: 198px;
    width: 204px; height: 56px;
    border-radius: 0 28px 28px 28px;
    background: linear-gradient(180deg, var(--orange-light), var(--orange));
    color: #fff;
    font-weight: 700;
    font-size: 20px;
    display: flex; align-items: center; justify-content: center;
    text-decoration: none;
    box-shadow: 0 4px 6px rgba(0,0,0,0.25);
  }
</style>
</head>
<body>
  <section class="banner">
    <svg class="banner-art" width="1184" height="284" viewBox="0 0 1184 284">
      <defs>
        <linearGradient id="photoTone" x1="0" y1="0" x2="1" y2="1">
          <stop offset="0" stop-color="#e9e4d6"/>
          <stop offset="0.45" stop-color="#8a6a4c"/>
          <stop offset="1" stop-color="#5f8a3a"/>
        </linearGradient>
        <linearGradient id="fieldGreen" x1="0" y1="0" x2="0" y2="1">
          <stop offset="0" stop-color="#558f22"/>
          <stop offset="1" stop-color="#6ea823"/>
        </linearGradient>
        <radialGradient id="threatTone" cx="0.5" cy="0.45" r="0.6">
          <stop offset="0" stop-color="#e8b3a8"/>
          <stop offset="1" stop-color="#a24a40"/>
        </radialGradient>
      </defs>

      <path d="M300 150 C 420 140, 520 190, 640 170 C 760 150, 880 150, 1000 138 L 1000 284 L 300 284 Z" fill="url(#fieldGreen)"/>
      <path d="M300 148 C 420 138, 520 186, 640 166 C 760 146, 880 146, 1000 134" fill="none" stroke="var(--brown)" stroke-width="10"/>

      <path d="M0 0 L 270 0 C 330 60, 345 200, 290 284 L 0 284 Z" fill="var(--green)"/>
      <path d="M0 0 L 280 0 C 360 70, 360 210, 320 284 L 300 284 C 340 200, 330 70, 268 0 Z" fill="var(--brown)"/>
      <path d="M282 0 C 370 80, 372 210, 336 284 L 356 284 C 390 200, 380 70, 300 0 Z" fill="var(--green)"/>
      <path d="M0 0 L 262 0 C 320 60, 332 200, 282 284 L 0 284 Z" fill="url(#photoTone)" role="img" aria-label="Photo: smiling woman in a sun hat and sunglasses hugging a small dog wearing sunglasses in a sunny park"/>

      <path d="M1040 0 C 990 60, 975 160, 1000 284 L 1184 284 L 1184 0 Z" fill="var(--green)"/>
      <path d="M1052 0 C 1002 60, 990 160, 1014 284 L 1184 284 L 1184 0 Z" fill="var(--brown)"/>
      <path d="M1060 0 C 1012 60, 1000 160, 1024 284 L 1184 284 L 1184 0 Z" fill="var(--paper)"/>

      <g stroke="var(--red-ring)" fill="none">
        <circle cx="414" cy="173" r="34" fill="url(#threatTone)" stroke="none" role="img" aria-label="Microscope photo of parvovirus-infected cells"/>
        <circle cx="414" cy="173" r="34" stroke-width="5"/>
        <line x1="390" y1="149" x2="438" y2="197" stroke-width="5"/>

        <circle cx="516" cy="171" r="37" fill="url(#threatTone)" stroke="none" role="img" aria-label="Close-up photo of a flea"/>
        <circle cx="516" cy="171" r="37" stroke-width="5"/>
        <line x1="490" y1="145" x2="542" y2="197" stroke-width="5"/>

        <circle cx="624" cy="168" r="41" fill="url(#threatTone)" stroke="none" role="img" aria-label="Photo of intestinal worms"/>
        <circle cx="624" cy="168" r="41" stroke-width="5"/>
        <line x1="595" y1="139" x2="653" y2="197" stroke-width="5"/>

        <circle cx="744" cy="158" r="51" fill="url(#threatTone)" stroke="none" role="img" aria-label="Close-up photo of a tick"/>
        <circle cx="744" cy="158" r="51" stroke-width="6"/>
        <line x1="708" y1="122" x2="780" y2="194" stroke-width="6"/>

        <circle cx="878" cy="149" r="57" fill="url(#threatTone)" stroke="none" role="img" aria-label="Photo of a heart infested with heartworms"/>
        <circle cx="878" cy="149" r="57" stroke-width="6"/>
        <line x1="838" y1="109" x2="918" y2="189" stroke-width="6"/>
      </g>
    </svg>

    <h1 class="headline">SPRING IS PERFECT FOR PETS, <span class="accent">AND PARASITES</span></h1>
    <p class="subline"><strong>Call us or Book online</strong> to protect your pets<br>from internal and external parasites.</p>

    <span class="threat-label" style="left:414px">PARVO</span>
    <span class="threat-label" style="left:516px">FLEAS</span>
    <span class="threat-label" style="left:624px">INTESTINAL<br>WORMS</span>
    <span class="threat-label" style="left:744px">TICKS</span>
    <span class="threat-label" style="left:878px">HEART WORM</span>

    <div class="brand">
      <div class="brand-dot"></div>
      <p class="brand-name">MEADOWBROOK<br>PET HOSPITAL</p>
    </div>

    <a class="book-online" href="#">BOOK ONLINE</a>
  </section>
</body>
</html>
```